Design a website for a newly developed Delta 8 THC Company

Design a responsive Website with the following goals in mind:
- Built on Wordpress/WooCommerce theme. Please use this when designing for ease of integration.
- Build trust with website visitors with an engaging, informative content driven website, that leads to a conversion of product purchase and repeat business. We will also be driving consumers to businesses that carry our products as well.
- The website will embody a lifestyle feel and make the visitor identify with the content.
- The website will allow for super charged SEO and other digital marketing and advertising strategies and tactics used to increase discovery, awareness, and conversion.
Please see additional goals in the uploaded files.
Target Market(s)
Male/Female 21-
Industry/Entity Type
Cannabis/Hemp
Coding
Coded - Design and coding required
Number of Pages Required
5+ page
Font styles to use
Other font styles liked:
- Montserrat
Look and feel
Each slider illustrates characteristics of the customer's brand and the style your logo design should communicate.

```html
<!DOCTYPE html>
<html lang="en">
<head>
<meta charset="utf-8">
<title>Solace — Contact</title>
<link href="https://fonts.googleapis.com/css2?family=Playfair+Display:wght@700&family=Poppins:wght@400;500;600&display=swap" rel="stylesheet">
<style>
:root{
  --gold:#c09a3a;
  --gold-light:#ecdb7e;
  --gold-dark:#bb9232;
  --ink:#111111;
  --text:#2c2c2c;
  --muted:#6a6a6a;
  --page:#f4f4f4;
  --field-border:#cfcfcf;
  --footer:#3a3b3d;
  --footer-text:#e6e6e6;
  --footer-muted:#bdbdbd;
  --base:#f5f4f2;
}
*{box-sizing:border-box;margin:0;padding:0}
html,body{width:1200px;height:1034px;overflow:hidden}
body{position:relative;font-family:'Poppins',sans-serif;background:var(--page);color:var(--text)}
.abs{position:absolute}

.promo-bar{left:0;top:0;width:1200px;height:31px;background:linear-gradient(90deg,var(--gold-light),var(--gold-dark));
  font-size:12px;font-weight:500;line-height:31px;text-align:center;color:#2b2410}

.brand{left:156px;top:60px;font-size:18px;font-weight:600;letter-spacing:4px;color:var(--ink);display:flex;align-items:center;gap:7px}
.brand-dot{width:10px;height:10px;border-radius:50%;background:var(--ink)}
.main-nav{top:57px;left:665px;display:flex;gap:36px;font-size:11.5px;font-weight:500;color:var(--ink)}
.icon-search{left:987px;top:56px}
.icon-cart{left:1018px;top:55px}
.cart-count{left:1031px;top:55px;width:9px;height:9px;border-radius:50%;background:var(--gold);font-size:6px;line-height:9px;text-align:center;color:#fff}

.hero-title{left:0;top:146px;width:1200px;text-align:center;font-family:'Playfair Display',serif;font-weight:700;font-size:44px;color:var(--ink);letter-spacing:-.3px}

.section-title{top:234px;font-family:'Playfair Display',serif;font-weight:700;font-size:36px;color:var(--gold);white-space:nowrap}
.intro{left:159px;top:290px;width:300px;font-size:14.5px;line-height:19.5px;color:var(--text)}

.field{background:#fff;border:1px solid var(--field-border);font-size:10.5px;color:#555;padding:0 10px;line-height:33px}
.field-message{line-height:normal;padding-top:9px}
.send-btn{left:156px;top:558px;width:131px;height:37px;border-radius:19px;background:linear-gradient(90deg,#f2e66a,var(--gold-dark));
  font-size:10.5px;font-weight:600;text-align:center;line-height:37px;color:#1a1a1a;letter-spacing:.3px}

.contact-card{left:641px;top:294px;width:398px;height:191px;background:#fff}
.contact-line{left:709px;font-size:13px;line-height:20px;color:#555}
.contact-icon{left:681px}
.card-emblem{left:889px;top:376px;width:146px;height:142px;border-radius:50%;background:radial-gradient(circle,#f3e591 0%,#d2b350 60%,rgba(210,179,80,.15) 100%)}

.site-footer{left:0;top:667px;width:1200px;height:314px;background:var(--footer)}
.footer-brand{left:156px;top:752px;font-size:16px;font-weight:600;letter-spacing:4px;color:var(--gold-light);display:flex;align-items:center;gap:7px}
.footer-brand .brand-dot{background:var(--gold-light)}
.footer-about{left:157px;top:807px;width:320px;font-size:10.5px;line-height:18px;color:var(--footer-text)}
.social{top:889px;width:38px;height:38px;border-radius:50%;border:1px solid #5a5b5e}
.footer-nav{left:782px;top:768px;display:flex;flex-direction:column;gap:9.5px;font-size:12px;color:var(--footer-text)}
.footer-heading{left:911px;top:764px;font-size:10.5px;font-weight:600;color:#fff}
.footer-line{left:929px;font-size:10px;line-height:16px;color:var(--footer-muted)}
.footer-icon{left:909px}

.base-bar{left:0;top:981px;width:1200px;height:53px;background:var(--base);text-align:center;font-size:8.5px;line-height:53px;color:#555}
</style>
</head>
<body>

<div class="abs promo-bar">Solace Delta 8 Premium Gummies</div>

<header>
  <div class="abs brand"><span class="brand-dot"></span>SOLACE</div>
  <nav class="abs main-nav"><span>HOME</span><span>OUR STORY</span><span>SHOP</span><span>CONTACT US</span></nav>
  <svg class="abs icon-search" width="17" height="17" viewBox="0 0 17 17" fill="none" stroke="#111" stroke-width="1.6"><circle cx="7" cy="7" r="5.5"/><path d="M11 11l5 5"/></svg>
  <svg class="abs icon-cart" width="22" height="20" viewBox="0 0 22 20" fill="none" stroke="#111" stroke-width="1.4"><path d="M1 2h3l3 11h11l2-8H6"/><circle cx="9" cy="17" r="1.5"/><circle cx="17" cy="17" r="1.5"/></svg>
  <div class="abs cart-count">0</div>
</header>

<h1 class="abs hero-title">LET’S DO SOMETHING AMAZING</h1>

<h2 class="abs section-title" style="left:156px">Contact Us</h2>
<p class="abs intro">Lorem ipsum dolor sit amet, consectetur adipiscing elit, sed do eiusmod</p>

<form>
  <div class="abs field" style="left:156px;top:350px;width:195px;height:35px">First Name</div>
  <div class="abs field" style="left:364px;top:350px;width:195px;height:35px">Email</div>
  <div class="abs field" style="left:156px;top:395px;width:195px;height:35px">Address</div>
  <div class="abs field" style="left:364px;top:395px;width:195px;height:35px">Phone</div>
  <div class="abs field field-message" style="left:156px;top:441px;width:403px;height:85px">Message</div>
  <div class="abs send-btn">SEND</div>
</form>

<h2 class="abs section-title" style="left:643px">Get Connect With Us</h2>
<div class="abs contact-card"></div>
<svg class="abs contact-icon" style="top:327px" width="14" height="17" viewBox="0 0 14 17" fill="none" stroke="#c9a93c" stroke-width="1.3"><path d="M7 16s5.5-5.5 5.5-9.5a5.5 5.5 0 0 0-11 0C1.5 10.5 7 16 7 16z"/><circle cx="7" cy="6.5" r="2"/></svg>
<div class="abs contact-line" style="top:322px">48 Amberline Way,<br>Suite 210, Larkfield,<br>ID 83990</div>
<svg class="abs contact-icon" style="top:397px" width="15" height="15" viewBox="0 0 15 15" fill="none" stroke="#c9a93c" stroke-width="1.3"><path d="M2 1.5l3 .5 1 3-1.5 1.5a8 8 0 0 0 4 4L10 9l3 1 .5 3c-6 1-13-6-11.5-11.5z"/></svg>
<div class="abs contact-line" style="top:393px">555-014-2290</div>
<svg class="abs contact-icon" style="top:433px" width="15" height="12" viewBox="0 0 15 12" fill="none" stroke="#c9a93c" stroke-width="1.3"><rect x="1" y="1" width="13" height="10"/><path d="M1 1l6.5 5.5L14 1"/></svg>
<div class="abs contact-line" style="top:426px">hello@solacegummies.com</div>
<div class="abs card-emblem" role="img" aria-label="Large gold brand emblem decoration"></div>

<footer>
  <div class="abs site-footer"></div>
  <div class="abs footer-brand"><span class="brand-dot"></span>SOLACE</div>
  <p class="abs footer-about">Sed diam nonummy nibh euismod tincidunt ut laoreet dolore magna aliquam erat volutpat widsi enim ad minim.</p>
  <div class="abs social" style="left:162px" aria-label="Social profile link"></div>
  <div class="abs social" style="left:207px" aria-label="Social profile link"></div>
  <div class="abs social" style="left:252px" aria-label="Social profile link"></div>

  <nav class="abs footer-nav"><span>Home</span><span>Our Story</span><span>Shop</span><span>Contact Us</span></nav>

  <div class="abs footer-heading">Solace Delta 8 Gummies</div>
  <svg class="abs footer-icon" style="top:800px" width="12" height="14" viewBox="0 0 14 17" fill="none" stroke="#d8c04a" stroke-width="1.4"><path d="M7 16s5.5-5.5 5.5-9.5a5.5 5.5 0 0 0-11 0C1.5 10.5 7 16 7 16z"/><circle cx="7" cy="6.5" r="2"/></svg>
  <div class="abs footer-line" style="top:795px">48 Amberline Way,<br>Suite 210, Larkfield,<br>ID 83990</div>
  <svg class="abs footer-icon" style="top:858px" width="13" height="13" viewBox="0 0 15 15" fill="none" stroke="#d8c04a" stroke-width="1.4"><path d="M2 1.5l3 .5 1 3-1.5 1.5a8 8 0 0 0 4 4L10 9l3 1 .5 3c-6 1-13-6-11.5-11.5z"/></svg>
  <div class="abs footer-line" style="top:856px">555-014-2290</div>
  <svg class="abs footer-icon" style="top:882px" width="13" height="10" viewBox="0 0 15 12" fill="none" stroke="#d8c04a" stroke-width="1.4"><rect x="1" y="1" width="13" height="10"/><path d="M1 1l6.5 5.5L14 1"/></svg>
  <div class="abs footer-line" style="top:879px">hello@solacegummies.com</div>
</footer>

<div class="abs base-bar">© 2021 Solace</div>

</body>
</html>
```